Re-design of website

I have an existing website that I would like to improve. The functionality will remain the same but the overall look will need to be changed. I have some ideas of what i would like included and am also in need of someone else to input their own creative ideas. I am on a tight deadline to get these improvements made as I have many people being directed to the site via our advertising campaigns that are in full swing late next week. Thanks
Target Market(s)
The website provides a virtual space for families to learn more about our learning program which we operate out of Dubai and will soon spread to the other Emirates. The families are generally between 25-50 year old parents with children up to the age of 6. They are local Emirati's as well as expats.

```html
<!DOCTYPE html>
<html lang="en">
<head>
<meta charset="utf-8">
<title>Little Grove — Home</title>
<link rel="stylesheet" href="https://fonts.googleapis.com/css2?family=Oswald:wght@500&family=Arimo:wght@400;700&family=Lora&display=swap">
<style>
  :root {
    --navy: #1c3d6e;
    --navy-deep: #15315b;
    --band: rgba(28, 61, 110, 0.92);
    --white: #ffffff;
    --ink: #1d1d1d;
    --muted: #555555;
    --rule: #9a9a9a;
    --olive: #6f8a1e;
    --olive-text: #7c8f2a;
  }
  * { box-sizing: border-box; margin: 0; padding: 0; }
  html, body { width: 1200px; height: 1000px; overflow: hidden; background: var(--white); }
  body { font-family: "Arimo", Arial, sans-serif; color: var(--ink); }

  .site { width: 1200px; height: 1000px; position: relative; overflow: hidden; }

  /* Hero */
  .hero { position: relative; height: 520px; }
  .hero-photo {
    position: absolute; inset: 0;
    background:
      radial-gradient(ellipse 260px 200px at 62% 18%, rgba(150, 60, 70, 0.75), transparent 70%),
      radial-gradient(ellipse 300px 260px at 45% 70%, rgba(40, 40, 38, 0.9), transparent 75%),
      radial-gradient(ellipse 220px 180px at 85% 35%, rgba(170, 140, 60, 0.55), transparent 70%),
      radial-gradient(ellipse 200px 160px at 12% 25%, rgba(120, 140, 70, 0.6), transparent 70%),
      linear-gradient(160deg, #3d4a22 0%, #27331a 45%, #1c2414 100%);
  }

  .brand {
    position: absolute; left: 50%; top: 150px; transform: translateX(-50%);
    display: flex; align-items: center; gap: 10px;
    font-weight: 700; font-size: 20px; color: var(--white);
  }
  .brand-dot { width: 22px; height: 22px; border-radius: 50%; background: var(--white); }

  .nav {
    position: absolute; left: 130px; top: 200px; width: 940px; height: 80px;
    display: flex;
  }
  .nav-links {
    flex: 1; background: var(--white); border-radius: 10px 0 0 10px;
    display: flex; align-items: center; justify-content: space-around; padding: 0 18px;
    list-style: none;
  }
  .nav-links li { font-weight: 700; font-size: 13px; letter-spacing: 0.2px; color: var(--ink); }
  .nav-links li.current { color: var(--navy); }
  .nav-search {
    width: 170px; background: var(--navy-deep); border-radius: 0 12px 12px 0;
    display: flex; align-items: center; justify-content: center;
  }

  .tagline-band {
    position: absolute; left: 0; right: 0; bottom: 0; height: 58px;
    background: var(--band);
    display: flex; align-items: center; justify-content: center; gap: 34px;
  }
  .tagline { color: var(--white); font-weight: 700; font-size: 15px; }
  .social { display: flex; gap: 10px; }
  .social span {
    width: 26px; height: 26px; border-radius: 50%; background: var(--white);
    display: flex; align-items: center; justify-content: center;
  }

  /* Content */
  .content { width: 880px; margin: 0 auto; padding-top: 34px; }

  .section-head { display: flex; flex-direction: column; align-items: center; }
  .section-head .ornament-line { display: flex; align-items: center; gap: 14px; }
  .section-head .ornament-line i { display: block; width: 140px; height: 1px; background: var(--rule); }
  .section-title {
    font-family: "Oswald", "Arial Narrow", sans-serif; font-weight: 500;
    color: var(--navy); font-size: 28px; letter-spacing: 0.5px; margin-top: 4px;
  }

  .post { display: flex; gap: 30px; margin: 22px 0 0 50px; }
  .post-media { position: relative; width: 150px; height: 150px; flex: none; }
  .post-photo { position: absolute; inset: 10px; background: linear-gradient(135deg, #2a2a2a, #0d0d0d); }
  .post-media .corner { position: absolute; width: 24px; height: 24px; border-color: var(--navy); border-style: solid; }
  .corner.tl { top: 0; left: 0; border-width: 3px 0 0 3px; }
  .corner.br { bottom: 0; right: 0; border-width: 0 3px 3px 0; }
  .post-body { width: 600px; }
  .post-title { font-family: "Lora", Georgia, serif; color: var(--olive-text); font-size: 17px; letter-spacing: 0.5px; margin-top: 4px; }
  .post-text { font-size: 12px; line-height: 1.55; color: var(--muted); margin-top: 10px; }
  .read-more { display: block; text-align: right; font-size: 10px; font-weight: 700; color: var(--navy); margin-top: 8px; letter-spacing: 0.4px; }

  .divider { display: flex; align-items: center; gap: 14px; margin-top: 26px; }
  .divider i { flex: 1; height: 1px; background: var(--rule); }
  .divider .badge { width: 28px; height: 28px; border-radius: 50%; background: var(--olive); display: flex; align-items: center; justify-content: center; }
  .divider h3 { font-size: 15px; font-weight: 700; letter-spacing: 0.3px; }

  .facts { display: flex; gap: 70px; margin: 20px 0 0 40px; }
  .fact-clients { display: flex; gap: 16px; width: 320px; }
  .world-map { width: 120px; height: 80px; margin-top: 26px; background: linear-gradient(90deg, #222, #444); border-radius: 30px 40px 20px 35px; }
  .fact-heading { font-size: 15px; font-weight: 700; line-height: 1.2; }
  .fact-list { list-style: none; font-size: 12px; color: var(--muted); margin-top: 8px; line-height: 1.35; }
  .fact-price { width: 400px; }
  .fact-price .fact-heading { display: flex; align-items: center; gap: 12px; }
  .fact-price .badge { width: 30px; height: 30px; border-radius: 50%; background: var(--olive); color: var(--white); font-size: 16px; display: flex; align-items: center; justify-content: center; }
  .fact-price p { font-size: 12px; line-height: 1.55; color: var(--muted); margin-top: 12px; }

  .next-head { margin-top: 34px; }
  .next-head .ornament-line i { width: 560px; background: var(--olive); }
</style>
</head>
<body>
<div class="site">
  <header class="hero">
    <div class="hero-photo" role="img" aria-label="Photo of a young child in a red hat holding a butterfly in an autumn forest"></div>

    <div class="brand"><span class="brand-dot"></span>Little Grove</div>

    <nav class="nav">
      <ul class="nav-links">
        <li class="current">HOME</li>
        <li>OUR METHOD</li>
        <li>THE PROGRAM</li>
        <li>MEDIA</li>
        <li>LOCATIONS</li>
        <li>ABOUT US</li>
        <li>CONTACT US</li>
      </ul>
      <div class="nav-search" aria-label="Search">
        <svg width="38" height="38" viewBox="0 0 38 38"><circle cx="22" cy="15" r="10" fill="none" stroke="#fff" stroke-width="3.5"/><line x1="15" y1="22" x2="5" y2="33" stroke="#fff" stroke-width="4" stroke-linecap="round"/></svg>
      </div>
    </nav>

    <div class="tagline-band">
      <p class="tagline">our philosophy and curriculum supports like-minded parents who want happiness for their children</p>
      <div class="social">
        <span aria-label="Social link"></span>
        <span aria-label="Social link"></span>
        <span aria-label="Email">
          <svg width="14" height="10" viewBox="0 0 14 10"><rect x="0.5" y="0.5" width="13" height="9" fill="none" stroke="#1c3d6e"/><polyline points="0.5,0.5 7,6 13.5,0.5" fill="none" stroke="#1c3d6e"/></svg>
        </span>
      </div>
    </div>
  </header>

  <main class="content">
    <section>
      <div class="section-head">
        <div class="ornament-line">
          <i></i>
          <svg width="10" height="14" viewBox="0 0 10 14"><path d="M5 0 C10 4 9 10 4 14 C1 10 1 4 5 0Z" fill="#6f8a1e"/></svg>
          <i></i>
        </div>
        <h2 class="section-title">FIRST RECENTES</h2>
      </div>

      <article class="post">
        <div class="post-media">
          <span class="corner tl"></span>
          <div class="post-photo" role="img" aria-label="Black and white portrait photo"></div>
          <span class="corner br"></span>
        </div>
        <div class="post-body">
          <h3 class="post-title">DUMMY ADDRESS</h3>
          <p class="post-text">Sam is not directly tied to the Lumo project. He is an independent support adviser for Lumo and for voice services in general to some degree. More importantly he is a kind person and quite possibly the finest adviser there is out there, anywhere. Sam is not tied to Lumo either; he simply helps families find answers.</p>
          <a class="read-more">READ MORE</a>
        </div>
      </article>
    </section>

    <div class="divider">
      <i></i>
      <span class="badge"><svg width="16" height="12" viewBox="0 0 16 12"><path d="M1 4 L8 1 L15 4 L8 7Z M4 6 V9 C6 11 10 11 12 9 V6" fill="#fff"/></svg></span>
      <h3>ABOUT MY HISTORY AND PRICES</h3>
      <i></i>
    </div>

    <section class="facts">
      <div class="fact-clients">
        <div class="world-map" role="img" aria-label="World map silhouette"></div>
        <div>
          <h4 class="fact-heading">MY CLIENTS ARE LOCATED<br>EVERYWHERE</h4>
          <ul class="fact-list">
            <li>United States</li>
            <li>Manila (Philippines)</li>
            <li>Canada</li>
            <li>India</li>
          </ul>
        </div>
      </div>
      <div class="fact-price">
        <h4 class="fact-heading"><span class="badge">$</span>HOW MUCH DO I CHARGE?</h4>
        <p>I get the majority of my work through referrals, and I have reference services available all your request. The rest of my business comes from this short letter and its associated advertisement on Searchly.</p>
      </div>
    </section>

    <div class="section-head next-head">
      <div class="ornament-line"><i></i></div>
      <h2 class="section-title">THIRD RECENTES</h2>
    </div>
  </main>
</div>
</body>
</html>
```